We want to a home page of our company in Tradevoro.com

We sell both home textile and hotel linen, but we are more professional on hotel linen , we want to make this page to be a very global style that is in the line of buyers reading habits , we want to show them that we are very professional on this business line, and the page must be very elegant and stylish
our current page is https://pelmistore.en.tradevoro.example/?spm=a2700.shop_cp.88.16 which i dont like , we want to make it international style and colors not so shine but very north euro feeling and logical is very clear
You could select photos from outside
We have a lot of photos, if you need more photos you pls contact us
Europe/North America / Israel / South East Asia etc
1 page
- MY BRAND LOGO

```html
<!DOCTYPE html>
<html lang="en">
<head>
<meta charset="utf-8">
<title>Pelmi Textile – Hotel Linen</title>
<link rel="stylesheet" href="https://fonts.googleapis.com/css2?family=Roboto:ital,wght@0,400;0,500;0,700;1,400&family=Titan+One&display=swap">
<style>
:root{
  --orange:#ef6a22;
  --orange-nav:#f07a2c;
  --ink:#222;
  --muted:#777;
  --line:#e2e2e2;
  --panel:#f4f4f4;
  --dark:#3b3b3b;
  --dark-2:#333;
  --white:#fff;
}
*{box-sizing:border-box;margin:0;padding:0}
html,body{width:1200px;height:3838px;overflow:hidden}
body{position:relative;background:var(--white);font-family:Roboto,Arial,sans-serif;color:var(--ink)}
.abs{position:absolute}
.photo{position:absolute;background:linear-gradient(160deg,#dfe3e8,#9aa2ab)}
.brand-name{font-family:Roboto,sans-serif;font-weight:700;color:var(--orange);letter-spacing:1px}
/* header */
.logo{left:145px;top:14px;font-size:44px;line-height:54px}
.search{left:432px;top:21px;width:400px;height:42px;border:1px solid #ccc;border-radius:21px;font-size:11px;color:#555;padding:14px 20px}
.search-btn{right:4px;top:5px;width:30px;height:30px;border-radius:50%;background:#333}
.account{left:860px;top:33px;font-size:13px;color:#555}
.account b{color:var(--orange);font-weight:400}
.nav{left:0;top:83px;width:1200px;height:41px;background:var(--orange-nav)}
.nav ul{list-style:none;display:flex;position:absolute;left:145px;top:0;height:41px}
.nav li{color:#fff;font-size:13px;font-weight:500;line-height:41px;padding:0 16px}
.nav li.active{background:#404040}
.currency{right:145px;top:0;line-height:41px;color:#fff;font-size:13px}
/* hero */
.categories{left:143px;top:140px;width:246px;height:483px;background:var(--panel);border:1px solid var(--line)}
.categories h2{position:absolute;left:44px;top:16px;font-size:21px;font-weight:700}
.cat{position:absolute;left:44px;display:flex;align-items:center;gap:22px;font-size:12px;font-weight:500}
.hex{width:68px;height:76px;clip-path:polygon(50% 0,100% 25%,100% 75%,50% 100%,0 75%,0 25%)}
.slider{left:399px;top:140px;width:657px;height:483px;background:linear-gradient(120deg,#1d2d55 0%,#2c3f6e 45%,#b7bccb 75%,#e4e6ee 100%)}
.slider-title{left:515px;top:250px;font-family:'Titan One',sans-serif;font-size:56px;line-height:60px;color:transparent;-webkit-text-stroke:2px var(--orange)}
.slider-sub{left:517px;top:403px;font-size:26px;font-weight:500;color:#fff}
.btn{background:var(--orange);color:#fff;font-weight:700;text-align:center}
.shop{left:519px;top:461px;width:128px;height:43px;line-height:43px;font-size:13px}
/* section titles */
.sec-title{position:absolute;left:140px;font-family:'Titan One',sans-serif;font-size:46px;color:#fff;-webkit-text-stroke:2px var(--orange)}
.sec-rule{position:absolute;height:6px;background:var(--line);right:143px}
/* products */
.card{position:absolute;width:218px;text-align:center}
.card .photo{position:relative;height:155px;border:1px solid #ccc}
.play{position:absolute;left:50%;top:50%;width:34px;height:34px;margin:-17px;border:2px solid #fff;border-radius:50%}
.play::after{content:"";position:absolute;left:12px;top:8px;border-left:11px solid #fff;border-top:7px solid transparent;border-bottom:7px solid transparent}
.card h3{font-size:16px;font-weight:500;margin-top:26px}
.price{font-size:10px;font-style:italic;color:var(--muted);margin-top:13px}
.more{display:inline-block;width:95px;height:29px;line-height:29px;font-size:10px;margin-top:17px}
/* about */
.about{left:145px;top:1502px;width:622px;height:413px;border:1px solid var(--line)}
.about p{position:absolute;left:40px;top:123px;width:385px;font-size:13px;line-height:25.6px;color:#666}
.frame{left:846px;top:1675px;width:264px;height:268px;border:3px solid var(--orange)}
.video{left:596px;top:1551px;width:459px;height:314px;background:linear-gradient(170deg,#6f737a,#c9cdd3 60%,#eceef0)}
.video .play{width:52px;height:52px;margin:-26px;border-width:3px}
.video .play::after{left:18px;top:13px;border-left-width:16px;border-top-width:10px;border-bottom-width:10px}
/* popular */
.pop{position:absolute;top:2171px;width:220px;height:250px;border:1px solid #ccc}
.pop .photo{position:relative;height:156px}
.pop h3{font-size:16px;font-weight:700;margin:18px 0 0 10px}
.pop .price{margin:8px 10px 0;text-align:left;line-height:17px}
/* brands */
.arrow-c{width:26px;height:26px;border:1px solid #999;border-radius:50%;font-size:14px;line-height:23px;text-align:center;color:#666}
.brand{position:absolute;top:2640px;width:130px;text-align:center;font-size:19px;color:#2a3a6a;font-weight:500}
/* testimonials */
.testi{position:absolute;top:2917px;width:298px;height:138px;border:1px solid var(--line);padding:22px 18px}
.testi p{font-size:10.5px;font-style:italic;line-height:19px;color:#666}
.testi .who{font-size:12px;color:var(--orange);margin-top:8px;font-weight:500}
.avatar{position:absolute;right:18px;top:104px;width:80px;height:90px;background:linear-gradient(#d7c3b4,#8a7b71)}
.stars{position:absolute;left:0;top:160px;font-size:14px;letter-spacing:3px;color:#f2b51f}
.stars span{color:#333}
.arrow-o{font-size:28px;color:#555}
/* footer */
.footer{left:0;top:3188px;width:1200px;height:650px;background:var(--dark)}
.news-title{position:absolute;width:1200px;text-align:center;top:95px;font-family:'Titan One',sans-serif;font-size:46px;color:transparent;-webkit-text-stroke:2px var(--orange)}
.news-text{position:absolute;width:1200px;text-align:center;top:169px;font-size:15px;color:#fff}
.email{left:322px;top:234px;width:556px;height:44px;background:#fff;border-radius:22px;font-size:13px;padding:15px 26px}
.subscribe{right:2px;top:2px;width:128px;height:40px;line-height:40px;border-radius:20px;font-size:14px}
.divider{left:0;top:340px;width:1200px;height:1px;background:#4a4a4a}
.pay{position:absolute;top:407px;width:31px;height:20px;border-radius:2px}
.social{position:absolute;top:401px;width:32px;height:32px;border-radius:50%;background:#fff}
.foot-nav{position:absolute;width:1200px;top:470px;text-align:center;color:#fff;font-size:15px;font-weight:500;word-spacing:6px}
.copy{position:absolute;width:1200px;top:515px;text-align:center;color:#ddd;font-size:11px}
.foot-logo{position:absolute;width:1200px;top:562px;text-align:center;font-size:44px}
</style>
</head>
<body>

<header>
  <div class="abs logo brand-name">Pelmi</div>
  <div class="abs search">Search Products<span class="abs search-btn"></span></div>
  <div class="abs account"><b>&#9679;</b> Sign In &nbsp;Join Free &nbsp;| &nbsp;<b>&#9632;</b> Cart(0)</div>
  <nav class="abs nav">
    <ul>
      <li class="active">HOME</li><li>PRODUCTS</li><li>PROFILE</li><li>CONTACTS</li><li>VIDEO</li><li>PROMOTION</li><li>FEEDS</li><li>VIEW MORE</li>
    </ul>
    <div class="abs currency">&#9679; USD &#9662;</div>
  </nav>
</header>

<section class="abs categories">
  <h2>CATEGORIES</h2>
  <div class="cat" style="top:62px"><div class="hex" role="img" aria-label="Bathrobe photo" style="background:linear-gradient(#c9c9cc,#8e8f95)"></div>BATHROBE</div>
  <div class="cat" style="top:143px"><div class="hex" role="img" aria-label="Towel photo" style="background:linear-gradient(#e8cfc6,#b68d80)"></div>TOWEL</div>
  <div class="cat" style="top:224px"><div class="hex" role="img" aria-label="Pillow photo" style="background:linear-gradient(#9ea3ab,#5d6068)"></div>PILLOW</div>
  <div class="cat" style="top:303px"><div class="hex" role="img" aria-label="F&amp;B linen photo" style="background:linear-gradient(#6b2a34,#2b1418)"></div>F&amp;B LINEN</div>
  <div class="cat" style="top:385px"><div class="hex" role="img" aria-label="Bedding photo" style="background:linear-gradient(#5a5a60,#c9c9cf)"></div>BEDDING</div>
</section>

<section>
  <div class="abs slider" role="img" aria-label="Hotel bedroom with white bed linen against a dark blue wall"></div>
  <div class="abs" style="left:430px;top:372px;color:#fff;font-size:26px">&#8249;</div>
  <div class="abs" style="left:1010px;top:366px;color:#fff;font-size:32px">&#8250;</div>
  <div class="abs slider-title">BEST QUALITY<br>HOTEL LINEN</div>
  <div class="abs slider-sub">Guest Room Bedding</div>
  <div class="abs btn shop">SHOP NOW</div>
</section>

<h2 class="sec-title" style="top:690px">FEATURED PRODUCTS</h2>
<div class="sec-rule" style="top:717px;left:665px"></div>

<section>
  <div class="card" style="left:145px;top:809px"><div class="photo" role="img" aria-label="White hotel bed set"><span class="play"></span></div><h3>PRODUCT NAME</h3><p class="price">$28.00 - $56.00/Set 10.0 Sets(Min. Order)</p><span class="btn more">VIEW MORE</span></div>
  <div class="card" style="left:376px;top:809px"><div class="photo" role="img" aria-label="White bed set with lace trim"><span class="play"></span></div><h3>PRODUCT NAME</h3><p class="price">$28.00 - $56.00/Set 10.0 Sets(Min. Order)</p><span class="btn more">VIEW MORE</span></div>
  <div class="card" style="left:606px;top:809px"><div class="photo" role="img" aria-label="Bed set with grey border"><span class="play"></span></div><h3>PRODUCT NAME</h3><p class="price">$28.00 - $56.00/Set 10.0 Sets(Min. Order)</p><span class="btn more">VIEW MORE</span></div>
  <div class="card" style="left:837px;top:809px"><div class="photo" role="img" aria-label="Bed set with dark stripe" style="background:linear-gradient(160deg,#c7b9b3,#7d6d69)"><span class="play"></span></div><h3>PRODUCT NAME</h3><p class="price">$28.00 - $56.00/Set 10.0 Sets(Min. Order)</p><span class="btn more">VIEW MORE</span></div>

  <div class="card" style="left:145px;top:1120px"><div class="photo" role="img" aria-label="White bed with navy runner"><span class="play"></span></div><h3>PRODUCT NAME</h3><p class="price">$28.00 - $56.00/Set 10.0 Sets(Min. Order)</p><span class="btn more">VIEW MORE</span></div>
  <div class="card" style="left:376px;top:1120px"><div class="photo" role="img" aria-label="White pillow with grey band" style="background:linear-gradient(160deg,#f3f3f3,#a6a6a8)"><span class="play"></span></div><h3>PRODUCT NAME</h3><p class="price">$28.00 - $56.00/Set 10.0 Sets(Min. Order)</p><span class="btn more">VIEW MORE</span></div>
  <div class="card" style="left:606px;top:1120px"><div class="photo" role="img" aria-label="Bed set with embroidered border"><span class="play"></span></div><h3>PRODUCT NAME</h3><p class="price">$28.00 - $56.00/Set 10.0 Sets(Min. Order)</p><span class="btn more">VIEW MORE</span></div>
  <div class="card" style="left:837px;top:1120px"><div class="photo" role="img" aria-label="Bed set with rose trim" style="background:linear-gradient(160deg,#e4dde0,#a99096)"><span class="play"></span></div><h3>PRODUCT NAME</h3><p class="price">$28.00 - $56.00/Set 10.0 Sets(Min. Order)</p><span class="btn more">VIEW MORE</span></div>
</section>

<section>
  <div class="abs frame"></div>
  <div class="abs about">
    <h2 class="sec-title" style="left:38px;top:40px">ABOUT US</h2>
    <p>Pelmi Textile Co.,Ltd. was established on 2013, is a professional linen solution provider,devotes into whole range of hotel bed linen, bath linen and F&amp;B linen.We are much more concerned about products quality, services with our the best sincerity to meet different kind of requirements from markets all over the worldThe typical international hotel brands we ever cooperated are</p>
    <div class="abs btn" style="left:40px;top:320px;width:128px;height:39px;line-height:39px;font-size:13px">READ MORE</div>
  </div>
  <div class="abs video" role="img" aria-label="Linen factory workshop video"><span class="play"></span></div>
</section>

<h2 class="sec-title" style="top:2052px">MOST POPULAR</h2>
<div class="sec-rule" style="top:2079px;left:530px"></div>

<section>
  <div class="pop" style="left:145px"><div class="photo" role="img" aria-label="Bed with red accent pillows"></div><h3>PRODUCT NAME</h3><p class="price">$28.00 - $56.00/Set 10.0 Sets<br>(Min. Order)</p></div>
  <div class="pop" style="left:376px"><div class="photo" role="img" aria-label="Bed with mustard throw" style="background:linear-gradient(170deg,#e5e5e5,#b89a5b)"></div><h3>PRODUCT NAME</h3><p class="price">$28.00 - $56.00/Set 10.0 Sets<br>(Min. Order)</p></div>
  <div class="pop" style="left:606px"><div class="photo" role="img" aria-label="Bed with wooden headboard" style="background:linear-gradient(170deg,#2f3a3c,#6b4a35 50%,#e7e7e7)"></div><h3>PRODUCT NAME</h3><p class="price">$28.00 - $56.00/Set 10.0 Sets<br>(Min. Order)</p></div>
  <div class="pop" style="left:837px"><div class="photo" role="img" aria-label="Bed with pink linen" style="background:linear-gradient(170deg,#3a3a3d,#cdb3bb 60%)"></div><h3>PRODUCT NAME</h3><p class="price">$28.00 - $56.00/Set 10.0 Sets<br>(Min. Order)</p></div>
</section>

<h2 class="sec-title" style="top:2513px">OUR BRANDS</h2>
<div class="sec-rule" style="top:2540px;left:473px"></div>

<section>
  <div class="abs arrow-c" style="left:90px;top:2642px">&#8249;</div>
  <div class="brand" style="left:129px">Hallbrook</div>
  <div class="brand" style="left:277px">Stervale</div>
  <div class="brand" style="left:437px">Corvane</div>
  <div class="brand" style="left:612px">Fjordhaven</div>
  <div class="brand" style="left:778px">Daluna Bay</div>
  <div class="brand" style="left:942px">Sherwell</div>
  <div class="abs arrow-c" style="left:1082px;top:2642px">&#8250;</div>
</section>

<h2 class="sec-title" style="top:2796px">CUSTOMER TESTIMONIALS</h2>
<div class="sec-rule" style="top:2823px;left:777px"></div>

<section>
  <div class="abs arrow-o" style="left:78px;top:2966px">&#8678;</div>
  <div class="testi" style="left:133px"><p>" Nemo enim ipsam voluptatem quia voluptas sit aspernatur aut odit aut fugit, sed quia consequuntur magni dolores eos qui ratione voluptatem sequi nesciunt. Neque porro quisquam est, "</p><div class="who">- John Doe</div><div class="hex avatar" role="img" aria-label="Customer portrait"></div><div class="stars">&#9733;&#9733;&#9733;<span>&#9733;&#9733;</span></div></div>
  <div class="testi" style="left:452px"><p>" Nemo enim ipsam voluptatem quia voluptas sit aspernatur aut odit aut fugit, sed quia consequuntur magni dolores eos qui ratione voluptatem sequi nesciunt. Neque porro quisquam est, "</p><div class="who">- John Doe</div><div class="hex avatar" role="img" aria-label="Customer portrait" style="background:linear-gradient(#e39a6a,#b5553a)"></div><div class="stars">&#9733;&#9733;&#9733;<span>&#9733;&#9733;</span></div></div>
  <div class="testi" style="left:771px"><p>" Nemo enim ipsam voluptatem quia voluptas sit aspernatur aut odit aut fugit, sed quia consequuntur magni dolores eos qui ratione voluptatem sequi nesciunt. Neque porro quisquam est, "</p><div class="who">- John Doe</div><div class="hex avatar" role="img" aria-label="Customer portrait" style="background:linear-gradient(#a59486,#4a3d36)"></div><div class="stars">&#9733;&#9733;&#9733;<span>&#9733;&#9733;</span></div></div>
  <div class="abs arrow-o" style="left:1090px;top:2966px">&#8680;</div>
</section>

<footer class="abs footer">
  <h2 class="news-title">SIGN UP NEWSLETTER</h2>
  <p class="news-text">We treat every customer sincerely and hope we can have the opportunity to Cooperate</p>
  <div class="abs email">Enter Email<span class="abs btn subscribe">SUBSCRIBE</span></div>
  <div class="abs divider"></div>
  <span class="pay" style="left:398px;background:#d9dde6"></span>
  <span class="pay" style="left:438px;background:#d9dde6"></span>
  <span class="pay" style="left:477px;background:#d9dde6"></span>
  <span class="pay" style="left:517px;background:#d9dde6"></span>
  <span class="pay" style="left:557px;background:#d9dde6"></span>
  <span class="social" style="left:643px"></span>
  <span class="social" style="left:685px"></span>
  <span class="social" style="left:727px"></span>
  <span class="social" style="left:769px"></span>
  <p class="foot-nav">HOME &nbsp;/ &nbsp;PRODUCTS &nbsp;/ &nbsp;PROFILE &nbsp;/ &nbsp;CONTACTS &nbsp;/ &nbsp;VIDEO &nbsp;/ &nbsp;PROMOTION &nbsp;/ &nbsp;FEEDS &nbsp;/ &nbsp;VIEW MORE</p>
  <p class="copy">© 2021 Companyname. All rights reserved. &nbsp;| Privacy Policy &nbsp;| Terms and Use</p>
  <div class="foot-logo brand-name">Pelmi</div>
</footer>

</body>
</html>
```